Lena Corvel Business Card

I need a business card that reflects my current website: itslenacorvel.com and screenshot attached. If we keep the color scheme of the site and sample card below that would be ideal. The business card should include the information on the attached sample cards.

Industry/Entity Type

Business

```html
<!DOCTYPE html>
<html lang="en">
<head>
<meta charset="utf-8">
<title>Lena Corvel Business Card</title>
<link rel="stylesheet" href="https://fonts.googleapis.com/css2?family=Open+Sans:wght@400;700&display=swap">
<style>
  :root {
    --page-bg: #e6e3de;
    --card-white: #ffffff;
    --card-grey: #dcdcdc;
    --wave-orange: #f39a26;
    --band-blue-light: #35c6ee;
    --band-blue-mid: #1c9fe0;
    --band-blue-deep: #1f4fb8;
    --name-yellow: #f4ec1c;
    --text-white: #ffffff;
    --signature-ink: #3a3a3a;
    --signature-ink-soft: #6a6a6a;
  }
  * { margin: 0; padding: 0; box-sizing: border-box; }
  html, body {
    width: 1200px; height: 900px; overflow: hidden;
    background: var(--page-bg);
    font-family: "Open Sans", Arial, sans-serif;
  }
  .card {
    position: absolute; left: 100px; top: 164px;
    width: 1000px; height: 572px;
    overflow: hidden;
    box-shadow: 0 10px 30px rgba(0,0,0,0.18);
  }
  .card-shapes { position: absolute; inset: 0; width: 100%; height: 100%; }
  .signature-area {
    position: absolute; left: 96px; top: 168px;
    width: 290px; height: 78px; border-radius: 39px;
    background: linear-gradient(100deg, var(--signature-ink-soft), var(--signature-ink));
    opacity: 0.85;
  }
  .contact-block {
    position: absolute; right: 48px; top: 44px;
    text-align: right; color: var(--text-white);
    font-size: 24px; line-height: 38px;
  }
  .identity-block {
    position: absolute; left: 58px; top: 392px;
    color: var(--text-white);
  }
  .identity-name {
    color: var(--name-yellow); font-weight: 700;
    font-size: 36px; line-height: 44px; letter-spacing: 0.5px;
    text-transform: uppercase;
  }
  .identity-role { font-size: 23px; line-height: 30px; }
</style>
</head>
<body>
  <div class="card">
    <svg class="card-shapes" viewBox="0 0 1000 572" preserveAspectRatio="none" aria-hidden="true">
      <defs>
        <linearGradient id="card-face" x1="0" y1="0" x2="1" y2="1">
          <stop offset="0" stop-color="var(--card-white)"/>
          <stop offset="1" stop-color="var(--card-grey)"/>
        </linearGradient>
        <linearGradient id="blue-band" x1="0" y1="0" x2="1" y2="0.3">
          <stop offset="0" stop-color="var(--band-blue-light)"/>
          <stop offset="0.5" stop-color="var(--band-blue-mid)"/>
          <stop offset="1" stop-color="var(--band-blue-deep)"/>
        </linearGradient>
      </defs>
      <rect width="1000" height="572" fill="url(#card-face)"/>
      <path d="M0,350 C230,345 360,280 440,170 C490,95 515,35 540,0 L1000,0 L1000,572 L0,572 Z" fill="var(--wave-orange)"/>
      <path d="M0,380 C250,378 400,310 480,200 C530,125 565,45 600,0 L1000,0 L1000,572 L0,572 Z" fill="url(#blue-band)"/>
    </svg>

    <div class="signature-area" role="img" aria-label="Handwritten script signature reading 'its Lena Corvel'"></div>

    <div class="contact-block">
      <p class="contact-email">hello@lenacorvel.com</p>
      <p class="contact-phone">555.014.2290</p>
      <p class="contact-social">[fb] | [t.] | [ig] @itslenacorvel</p>
      <p class="contact-web">www.itslenacorvel.com</p>
    </div>

    <div class="identity-block">
      <h1 class="identity-name">Lena Corvel</h1>
      <p class="identity-role">Brand Curator</p>
      <p class="identity-role">Digital Storyteller</p>
      <p class="identity-role">Social Entrprenuer</p>
    </div>
  </div>
</body>
</html>
```